Corporate Letterhead

Looking for a new corporate letterhead design. Our colors are orange and gray.

We'd like it if the below could be included somehow in the letterhead.                                       

Partnerships | Results | Quality

• Logo, Company Name, Address, Phone #, Fax #, Web address, Email address (optional), the phrase "A Service Disable Veteran Owned Small Business".

```html
<!DOCTYPE html>
<html lang="en">
<head>
<meta charset="utf-8">
<title>Vantara Systems, Inc — Letterhead</title>
<link href="https://fonts.googleapis.com/css2?family=Jost:wght@300;400;600&display=swap" rel="stylesheet">
<style>
  :root {
    --orange: #e8902a;
    --gray: #5f6062;
    --gray-light: #8a8b8d;
    --paper: #ffffff;
    --backdrop: #ececec;
  }
  * { margin: 0; padding: 0; box-sizing: border-box; }
  html, body {
    width: 1200px; height: 936px; overflow: hidden;
    background: var(--backdrop);
    font-family: "Jost", sans-serif;
  }
  .letterhead {
    position: absolute;
    left: 300px; top: 44px;
    width: 600px; height: 848px;
    background: var(--paper);
    box-shadow: 0 2px 10px rgba(0,0,0,0.08);
  }
  .brand {
    position: absolute;
    top: 58px; left: 0; width: 100%;
    display: flex; justify-content: center; align-items: center; gap: 10px;
  }
  .brand-dot {
    width: 22px; height: 22px; border-radius: 50%;
    background: var(--orange);
  }
  .brand-name {
    font-weight: 600; font-size: 22px; letter-spacing: 1.5px;
    color: var(--orange); line-height: 1;
  }
  .contact {
    position: absolute; top: 138px; left: 44px;
    font-size: 7.5px; line-height: 10px; color: var(--gray);
    font-weight: 400;
  }
  .contact .company { text-transform: uppercase; letter-spacing: 0.3px; }
  .contact ul { list-style: none; margin-top: 3px; }
  .contact li { display: flex; align-items: center; gap: 4px; }
  .contact li svg { width: 7px; height: 7px; flex: none; }
  .side-band {
    position: absolute; left: 0; top: 390px; bottom: 0;
    width: 7px; background: var(--orange);
  }
  .tagline {
    position: absolute;
    right: 22px; bottom: 30px;
    transform-origin: right bottom;
    transform: rotate(-90deg) translateX(100%);
    white-space: nowrap;
    font-weight: 300; font-size: 15px; letter-spacing: 1.2px;
    color: var(--gray); text-transform: uppercase;
  }
  .tagline .divider { color: var(--orange); margin: 0 6px; }
</style>
</head>
<body>
  <main class="letterhead">
    <header class="brand">
      <span class="brand-dot"></span>
      <span class="brand-name">VANTARA SYSTEMS, INC</span>
    </header>

    <address class="contact">
      <div class="company">Vantara Systems, Inc</div>
      <div>48 Mill Lane</div>
      <div>London, E9 4QT</div>
      <ul>
        <li><svg viewBox="0 0 10 10"><circle cx="5" cy="5" r="5" fill="var(--orange)"/></svg>020 7946 0321</li>
        <li><svg viewBox="0 0 10 10"><circle cx="5" cy="5" r="5" fill="var(--orange)"/></svg>07700 900 418</li>
        <li><svg viewBox="0 0 10 10"><circle cx="5" cy="5" r="5" fill="var(--orange)"/></svg>info@vantarasys.com</li>
        <li><svg viewBox="0 0 10 10"><circle cx="5" cy="5" r="5" fill="var(--orange)"/></svg>www.vantarasys.com</li>
      </ul>
    </address>

    <div class="side-band"></div>

    <p class="tagline">Partnerships<span class="divider">|</span>Results<span class="divider">|</span>Quality</p>
  </main>
</body>
</html>
```